I own a small business whose primary function is Professional Fashion and Commercial Photography and has a secondary function of Talent Management of Models/Actors. I've used PrintaNova in the past to print my own design, but I'd like something a bit more topical, fresh and done by an artist instead of a photographer (me).

My company logo is included with a few selected horizontal (landscape) photos of some of my models--I'd like to use a single model photo as the background for the entire card, either in color or converted to black and white, at opacity enough to see the photo but not too much to obscure any text or the company logo, or use a photo as a share of the card (not the entire background), or use all the three models on the card in some manor... Our company colors are white, black, grey-silver and red.

Industry/Entity Type

Small Business

Contact Information for Business Card

Darnell Voskuijl, Owner
KLT Studios
PO Box 7316
Millbrook VT 05999-7316
(555) 014-2273
dan@kltstudios-example,.com

```html
<!DOCTYPE html>
<html lang="en">
<head>
<meta charset="utf-8">
<title>KLT Studios – Business Card</title>
<link rel="stylesheet" href="https://fonts.googleapis.com/css2?family=Open+Sans:wght@400;600;700&display=swap">
<style>
  :root {
    --bg: #efefef;
    --black: #0b0b0b;
    --panel: #1a1a1a;
    --red: #e0392b;
    --red-deep: #b3262a;
    --white: #ffffff;
    --grey: #8a8a8a;
    --silver: #bdbdbd;
  }
  * { box-sizing: border-box; margin: 0; padding: 0; }
  html, body {
    width: 1200px; height: 1000px; overflow: hidden;
    background: var(--bg);
    font-family: "Open Sans", Arial, sans-serif;
  }
  .canvas { position: relative; width: 1200px; height: 1000px; }

  .card {
    position: absolute; left: 285px; width: 630px; height: 360px;
    overflow: hidden; box-shadow: 0 6px 18px rgba(0,0,0,.18);
  }

  /* ---------- back side ---------- */
  .card-back {
    top: 90px; background: var(--black);
    border-top: 5px solid var(--red); border-bottom: 5px solid var(--red);
  }
  .brand-plate {
    position: absolute; left: 56px; top: 96px; width: 290px; height: 62px;
    background: var(--white); display: flex; align-items: center; gap: 12px;
    padding-left: 18px;
  }
  .brand-mark { width: 26px; height: 26px; background: var(--red); flex: none; }
  .brand-name { font-weight: 700; font-size: 28px; color: var(--red); letter-spacing: .5px; }
  .identity { position: absolute; left: 56px; top: 178px; width: 290px; text-align: center; }
  .identity-name { color: var(--red); font-weight: 700; font-size: 21px; letter-spacing: -.3px; text-transform: uppercase; }
  .identity-role { color: var(--white); font-size: 12px; margin-top: 1px; }
  .identity-tagline { color: var(--red); font-weight: 700; font-size: 12.5px; margin-top: 12px; text-transform: uppercase; letter-spacing: -.2px; }

  .contact-list { position: absolute; left: 378px; top: 78px; width: 225px; display: flex; flex-direction: column; gap: 14px; }
  .contact-item {
    height: 62px; border: 2px solid var(--red); border-radius: 7px;
    background: var(--panel); display: flex; align-items: center; gap: 14px;
    padding: 0 12px; color: var(--white); font-size: 11.5px; line-height: 1.55;
  }
  .contact-item svg { width: 18px; height: 18px; flex: none; fill: var(--white); }

  /* ---------- front side ---------- */
  .card-front {
    top: 550px; background: var(--white);
    border-top: 5px solid var(--red); border-bottom: 5px solid var(--red);
  }
  .photo-row { position: absolute; inset: 0 0 auto 0; height: 225px; display: flex; }
  .photo { flex: 1; }
  .photo-one { background: linear-gradient(160deg, #b7372f, #8e1f1f); }
  .photo-two { background: linear-gradient(160deg, #4a4a4a, #2a2426 55%, #7c5a63); }
  .photo-three { background: linear-gradient(160deg, #7f9a56, #c9b9a3 60%, #c4322f); }
  .photo-strip {
    position: absolute; left: 0; right: 0; bottom: 0; height: 30px;
    background: linear-gradient(90deg, #b3262a 0 33%, #222 33% 66%, #b3262a 66%);
  }
  .brand-band {
    position: absolute; left: 0; right: 0; top: 225px; height: 95px;
    background: var(--white); display: flex; align-items: center; justify-content: center; gap: 16px;
  }
  .brand-band .brand-mark { width: 36px; height: 36px; }
  .brand-band .brand-name { font-size: 40px; }
</style>
</head>
<body>
<main class="canvas">

  <section class="card card-back" aria-label="Business card, contact side">
    <div class="brand-plate">
      <span class="brand-mark"></span>
      <span class="brand-name">KLT Studios</span>
    </div>
    <div class="identity">
      <p class="identity-name">Darnell Voskuijl</p>
      <p class="identity-role">Owner</p>
      <p class="identity-tagline">Wedding, Event, Potraits &amp; More</p>
    </div>
    <div class="contact-list">
      <div class="contact-item">
        <svg viewBox="0 0 24 24" aria-hidden="true"><path d="M12 3 2 12h3v9h5v-6h4v6h5v-9h3z"/></svg>
        <span>KLT Studios ,<br>PO Box 7316 Millbrook VT</span>
      </div>
      <div class="contact-item">
        <svg viewBox="0 0 24 24" aria-hidden="true"><path d="M6.6 10.8a15 15 0 0 0 6.6 6.6l2.2-2.2a1 1 0 0 1 1-.25 11.4 11.4 0 0 0 3.6.57 1 1 0 0 1 1 1V20a1 1 0 0 1-1 1A17 17 0 0 1 3 4a1 1 0 0 1 1-1h3.5a1 1 0 0 1 1 1c0 1.25.2 2.45.57 3.57a1 1 0 0 1-.25 1z"/></svg>
        <span>+ 05999-7316<br>+ (555) 014-2273</span>
      </div>
      <div class="contact-item">
        <svg viewBox="0 0 24 24" aria-hidden="true"><path d="M3 5h18v14H3zm2 2v.5l7 4.5 7-4.5V7zm0 2.9V17h14V9.9l-7 4.5z"/></svg>
        <span>dan@kltstudios-example,.com</span>
      </div>
    </div>
  </section>

  <section class="card card-front" aria-label="Business card, photo side">
    <div class="photo-row">
      <div class="photo photo-one" role="img" aria-label="Portrait of a young male model in a red top against a red backdrop"></div>
      <div class="photo photo-two" role="img" aria-label="Close portrait of a young male model wearing a black cap"></div>
      <div class="photo photo-three" role="img" aria-label="Outdoor portrait of a young male model in a red shirt"></div>
    </div>
    <div class="photo-strip" role="img" aria-label="Lower edge of the three model portraits"></div>
    <div class="brand-band">
      <span class="brand-mark"></span>
      <span class="brand-name">KLT Studios</span>
    </div>
  </section>

</main>
</body>
</html>
```